Business Advisory Firm Business Card

A clean, very upscale looking business card. Not crowded.

Please include logo (attached) and:

Daria K. Pellworth
Four Marlow Court
New York, NY 10023
tel: (917) 555-0143
fax: (646) 555-0172
email: dpellworth@quarrystoneconsultants.example
website: www.quarrystoneconsultants.example

Target Market(s)

Business clients. Often real estate development firms, other advisory firms or growing companies that need assistance. I would like a card that looks impressive and confident.

Industry/Entity Type

Business

Colors

Designer to choose colors to be used in the design.

Requirements
Must have
• Impressive and confident. Please include logo.
Should not have
• nothing flashy...

```html
<!DOCTYPE html>
<html lang="en">
<head>
<meta charset="utf-8">
<title>Quarrystone Advisory Services – Business Card</title>
<link rel="stylesheet" href="https://fonts.googleapis.com/css2?family=Bree+Serif&family=Crimson+Text:wght@700&display=swap">
<style>
  :root {
    --card-dark: #1b1b1b;
    --card-mid: #3a3a3a;
    --panel-light: #f3f3f3;
    --panel-shade: #d9d9d9;
    --brand-green: #3bb44a;
    --brand-green-deep: #2f9a3d;
    --ink: #1e1e1e;
    --contact-text: #f4f4f4;
    --icon: #ececec;
  }
  html, body {
    margin: 0;
    padding: 0;
    overflow: hidden;
    background: #ffffff;
  }
  .card {
    position: relative;
    width: 1200px;
    height: 686px;
    overflow: hidden;
    background: radial-gradient(ellipse 70% 75% at 42% 52%, var(--card-mid) 0%, #2a2a2a 45%, var(--card-dark) 100%);
  }
  .brand-panel {
    position: absolute;
    left: 77px;
    top: 0;
    width: 432px;
    height: 514px;
    border-radius: 0 0 34px 34px;
    background: linear-gradient(180deg, var(--panel-light) 0%, #eaeaea 55%, var(--panel-shade) 100%);
    box-shadow: 0 6px 18px rgba(0,0,0,0.35);
  }
  .brand-mark {
    position: absolute;
    left: 140px;
    top: 78px;
    width: 150px;
    height: 150px;
    background: var(--brand-green);
  }
  .brand-name {
    position: absolute;
    left: 48px;
    top: 296px;
    margin: 0;
    font-family: "Bree Serif", serif;
    font-weight: 400;
    font-size: 50px;
    line-height: 67px;
    color: var(--ink);
    letter-spacing: 0.3px;
  }
  .name-tab {
    position: absolute;
    left: 600px;
    top: 66px;
    width: 620px;
    height: 180px;
    background: linear-gradient(180deg, var(--brand-green) 0%, var(--brand-green-deep) 100%);
    border-radius: 34px 0 0 22px;
    box-shadow: 0 14px 22px rgba(0,0,0,0.45);
  }
  .person-name {
    position: absolute;
    left: 0;
    right: 20px;
    top: 50px;
    margin: 0;
    text-align: center;
    font-family: "Bree Serif", serif;
    font-weight: 400;
    font-size: 54px;
    line-height: 1;
    color: #ffffff;
  }
  .contact-list {
    position: absolute;
    left: 598px;
    top: 447px;
    margin: 0;
    padding: 0;
    list-style: none;
  }
  .contact-item {
    display: flex;
    align-items: center;
    height: 56px;
    font-family: "Crimson Text", serif;
    font-weight: 700;
    font-size: 23px;
    color: var(--contact-text);
    white-space: pre;
  }
  .contact-icon {
    width: 46px;
    height: 40px;
    margin-right: 22px;
    flex: none;
  }
</style>
</head>
<body>
<div class="card">
  <div class="brand-panel">
    <div class="brand-mark"></div>
    <p class="brand-name">Quarrystone<br>Advisory<br>Services, inc.</p>
  </div>

  <div class="name-tab">
    <h1 class="person-name">Daria K. Pellworth</h1>
  </div>

  <ul class="contact-list">
    <li class="contact-item">
      <svg class="contact-icon" viewBox="0 0 46 40" aria-hidden="true">
        <path d="M23 4 L4 20 L9 20 L9 36 L19 36 L19 26 L27 26 L27 36 L37 36 L37 20 L42 20 Z" fill="none" stroke="var(--icon)" stroke-width="3.5" stroke-linejoin="round"/>
      </svg>
      <span>Four Marlow Court, New York, NY 10023</span>
    </li>
    <li class="contact-item">
      <svg class="contact-icon" viewBox="0 0 46 40" aria-hidden="true">
        <rect x="11" y="2" width="22" height="36" rx="7" fill="var(--icon)"/>
        <rect x="15" y="9" width="14" height="14" rx="2" fill="#2b2b2b"/>
        <rect x="18" y="28" width="8" height="4" rx="2" fill="#2b2b2b"/>
      </svg>
      <span> (917) 555-0143 ;     Fax: (646) 555-0172 ;</span>
    </li>
    <li class="contact-item">
      <svg class="contact-icon" viewBox="0 0 46 40" aria-hidden="true">
        <rect x="4" y="7" width="36" height="26" fill="none" stroke="var(--icon)" stroke-width="3"/>
        <path d="M4 7 L22 22 L40 7 M4 33 L17 18 M40 33 L27 18" fill="none" stroke="var(--icon)" stroke-width="3"/>
      </svg>
      <span>dpellworth@quarrystoneconsultants.example</span>
    </li>
    <li class="contact-item">
      <svg class="contact-icon" viewBox="0 0 46 40" aria-hidden="true">
        <circle cx="20" cy="19" r="15" fill="none" stroke="var(--icon)" stroke-width="3"/>
        <ellipse cx="20" cy="19" rx="6.5" ry="15" fill="none" stroke="var(--icon)" stroke-width="2.5"/>
        <path d="M5 19 H35 M8 11 H32 M8 27 H32" stroke="var(--icon)" stroke-width="2.5"/>
        <path d="M27 22 L27 38 L31 34 L34 40 L37 39 L34 33 L39 33 Z" fill="var(--icon)" stroke="#222" stroke-width="1.5" stroke-linejoin="round"/>
      </svg>
      <span> www.quarrystoneconsultants.example</span>
    </li>
  </ul>
</div>
</body>
</html>
```